Payment company requires web design

We need a web design for a new company based in Singapore.

The company focuses on providing 2 key products: 1) an alternative payment option (i.e. like plorix or quentabank options) on the traditional checkout process 2) a replacement/outsource of a merchants payment page. Key in the UX flow is a end customer dashboard that manages all payments.

We look to provide a simple, fluid and easy to use payment process. The dashboard is minimalistic that allows easy navigation, review of transactions and all available options through gamification.

The final design should communicate ease of use, flexibility and transparency.

Target Market(s)

The value is for the merchant - retail/travel/insurance companies. However its the merchant's end customers that are the target and who the UX is built for.

Industry/Entity Type

It Company

Logo Text

dravin

Number of Pages Required

5+ page

Colors
ec1f27

Requirements
Must have
• 7 pages mimicking UX flow
• payment page * 2 - 1) alternative payment type 2) outsource of merchants payment page to our business
• our landing page
• end customer verification page
• end customer registration
• customer dashboard
• UX flow in attached file
Nice to have
• open to ideas
• have asked for the logo to be added
• logo to have the colour red (chinese for prosperity)
• the company is all about flexibility, transparency in personal finance management with the option of instalment payments

```html
<!DOCTYPE html>
<html lang="en">
<head>
<meta charset="utf-8">
<title>Demoshop Checkout</title>
<link href="https://fonts.googleapis.com/css2?family=Roboto:wght@400;500;700&family=Hind:wght@400;500;600&display=swap" rel="stylesheet">
<style>
:root{
  --ink:#1f2329;
  --header:#252a31;
  --accent:#d98a2b;
  --line:#d9d9d9;
  --muted:#7a7a7a;
  --text:#444;
  --brand-red:#ec1f27;
  --white:#fff;
}
*{box-sizing:border-box;margin:0;padding:0}
html,body{width:1200px;height:810px;overflow:hidden;background:var(--white)}
body{position:relative;font-family:'Hind',sans-serif;color:var(--text)}
.site-header{position:absolute;left:0;top:0;width:1200px;height:93px;background:var(--header);border-top:2px solid var(--accent)}
.wordmark{position:absolute;font-family:'Roboto',sans-serif;font-weight:700;font-size:24px;color:var(--accent);letter-spacing:.3px}
.site-header .wordmark{left:150px;top:31px}
.main-nav a{position:absolute;top:40px;font-family:'Roboto',sans-serif;font-weight:500;font-size:11px;color:var(--white);text-decoration:none;letter-spacing:.3px}
.header-icons svg{position:absolute}
.cart-badge{position:absolute;left:1025px;top:48px;width:14px;height:14px;border-radius:50%;background:var(--accent);color:var(--white);font:500 8px/14px 'Roboto',sans-serif;text-align:center}
.page-title{position:absolute;left:0;width:1200px;top:154px;text-align:center;font-family:'Roboto',sans-serif;font-weight:700;font-size:22px;color:var(--ink);letter-spacing:.5px}
.order-table{position:absolute;left:151px;top:232px;width:431px;border-collapse:collapse}
.order-table td,.order-table th{border:1px solid var(--line);padding:0 15px;text-align:left;vertical-align:middle}
.order-table th{height:38px;font:700 10px 'Roboto',sans-serif;color:var(--ink);letter-spacing:.3px}
.order-table .item td{height:39px;font-size:13px;color:var(--muted)}
.order-table .dark td{background:var(--header);color:var(--white);border-color:#444a52}
.order-table .dark td:first-child{font:700 10px 'Roboto',sans-serif;letter-spacing:.3px}
.order-table .dark td:last-child{font-size:13px}
.order-table .sum td{height:39px}
.order-table .ship td{height:68px}
.order-table .grand td{height:37px}
.ship-option{display:flex;align-items:center;gap:5px;font-size:11px;line-height:26px}
.dot{width:9px;height:9px;border-radius:50%;border:2px solid var(--white)}
.dot.on{background:var(--white)}
.col-left{width:215px}
.options-title{position:absolute;left:611px;top:229px;font:700 14px 'Roboto',sans-serif;color:var(--ink);letter-spacing:.4px}
.options-rule{position:absolute;left:612px;top:250px;width:38px;height:2px;background:var(--accent)}
.options{position:absolute;left:612px;top:280px;width:428px;border:1px solid var(--line)}
.option{height:45px;border-bottom:1px solid var(--line);display:flex;align-items:center;padding-left:19px;font-size:11px;color:var(--text);gap:5px}
.radio{width:9px;height:9px;border-radius:50%;border:1px solid #888;position:relative;flex:none}
.radio.on::after{content:"";position:absolute;left:1.5px;top:1.5px;width:4px;height:4px;border-radius:50%;background:#333}
.option.featured{height:115px;border-bottom:none;display:block;padding:12px 11px 0 19px;position:relative}
.featured-head{display:flex;align-items:center;gap:5px}
.partner-name{display:flex;align-items:center;gap:3px;font-weight:600;font-size:15px;color:var(--brand-red)}
.partner-name i{width:11px;height:11px;background:var(--brand-red);display:block}
.what-is{position:absolute;right:11px;top:15px;font-size:11px;color:var(--brand-red)}
.featured-copy{margin:22px 0 0 15px;font-size:11px;color:var(--muted);line-height:18px;width:370px;letter-spacing:.2px}
.cta{position:absolute;left:612px;top:591px;width:142px;height:38px;background:var(--header);color:var(--white);font:700 10px/38px 'Roboto',sans-serif;text-align:center;letter-spacing:.3px}
.site-footer{position:absolute;left:0;top:719px;width:1200px;height:91px;border-top:1px solid #e3c793}
.site-footer .wordmark{left:150px;top:32px}
.footer-nav a{position:absolute;top:40px;font:400 10px 'Roboto',sans-serif;color:var(--ink);text-decoration:none;letter-spacing:.4px}
.social{position:absolute;right:160px;top:40px;display:flex;gap:12px;font:500 9px 'Roboto',sans-serif;color:var(--ink)}
</style>
</head>
<body>
<header class="site-header">
  <div class="wordmark">DEMOSHOP</div>
  <nav class="main-nav">
    <a style="left:413px">HOME</a>
    <a style="left:489px">SHOP &#9662;</a>
    <a style="left:570px">BLOG</a>
    <a style="left:642px">SUPPORT</a>
    <a style="left:736px">CONTACT</a>
  </nav>
  <div class="header-icons">
    <svg style="left:972px;top:34px" width="21" height="21" viewBox="0 0 21 21" fill="none" stroke="#fff" stroke-width="1.4"><circle cx="8.5" cy="8.5" r="7"/><line x1="13.5" y1="13.5" x2="19.5" y2="19.5"/></svg>
    <svg style="left:1014px;top:34px" width="20" height="19" viewBox="0 0 20 19" fill="none" stroke="#fff" stroke-width="1.3"><path d="M1 2h3l2 10h11l2-7H5"/><line x1="7" y1="7" x2="17" y2="7"/><line x1="7" y1="9.5" x2="16" y2="9.5"/><circle cx="8" cy="16" r="1.5"/><circle cx="15" cy="16" r="1.5"/></svg>
    <div class="cart-badge">1</div>
  </div>
</header>

<h1 class="page-title">CHECKOUT</h1>

<table class="order-table">
  <tr><th class="col-left">PRODUCT</th><th>TOTAL</th></tr>
  <tr class="item"><td>Item A x 1</td><td>$75.00</td></tr>
  <tr class="item"><td>Item B x 2</td><td>$60.00</td></tr>
  <tr class="dark sum"><td>SUBTOTAL</td><td>$135.00</td></tr>
  <tr class="dark ship"><td>SHIPPING</td><td>
    <div class="ship-option"><span class="dot"></span>Flat Rate : $20.00</div>
    <div class="ship-option"><span class="dot on"></span>Free Shipping</div>
  </td></tr>
  <tr class="dark grand"><td>TOTAL</td><td>$155.00</td></tr>
</table>

<h2 class="options-title">PAYMENT OPTIONS</h2>
<div class="options-rule"></div>
<div class="options">
  <div class="option"><span class="radio"></span>Credit Card</div>
  <div class="option"><span class="radio"></span>Debit Card</div>
  <div class="option"><span class="radio"></span>Direct Bank Transfer</div>
  <div class="option"><span class="radio"></span>Cash on Delivery</div>
  <div class="option featured">
    <div class="featured-head"><span class="radio on"></span><span class="partner-name"><i></i>dravin</span></div>
    <span class="what-is">What is dravin?</span>
    <p class="featured-copy">Pay via dravin; Buy now and pay the total later at once or in easy installments</p>
  </div>
</div>
<div class="cta">BUY NOW PAY LATER</div>

<footer class="site-footer">
  <div class="wordmark">DEMOSHOP</div>
  <nav class="footer-nav">
    <a style="left:468px">TERMS &amp; CONDITIONS</a>
    <a style="left:626px">POLICY</a>
    <a style="left:709px">MAP</a>
  </nav>
  <div class="social"><span>Socio</span><span>Chirp</span><span>Gplex</span><span>Snapr</span></div>
</footer>
</body>
</html>
```